Business Card Design Project

looking for a stylish and simple double sided business card.
I am an artist - specialising in fashion illustration, portraits and murals.
the front should be simply my name and tag:

D U R E S K
Living in colour

My preference is for a Black background with DURESK in red or embossed.
Living in colour in White or multi-coloured.

the back will have detail:

Personalised Art
Portraits, Murals, Fashion Illustration

0437 582 190
duresk@duresk.com.au
www.duresk.com.au

Target Market(s)

Adults that are based in western speaking countries who have an appreciation for art and design. Portraits and wall art
Business owners who may need personalised all art for their business space. Murals and personalised canvass.
People in the fashion industry, who may require fashion illustrations.

Industry/Entity Type

Fashion

Requirements
Must have
• BOLD but simple at the same time, timeless modern element to it.
Nice to have
• simple lettering
Should not have
• Not too busy or wordy,

```html
<!DOCTYPE html>
<html lang="en">
<head>
<meta charset="utf-8">
<title>Duresk Business Card – Front and Back</title>
<link rel="stylesheet" href="https://fonts.googleapis.com/css2?family=Open+Sans:wght@400;700&family=Tinos:ital,wght@0,400;1,700&display=swap">
<style>
  :root {
    --backdrop: #1b1d1e;
    --card: #1f1f20;
    --card-edge: #2a2a2b;
    --red: #b3140f;
    --red-line: #a3120d;
    --text-light: #d8d8d8;
    --text-muted: #bdbdbd;
    --c1: #e8b400;
    --c2: #4fc3e8;
    --c3: #3b6be0;
    --c4: #8a3ad0;
    --c5: #1f9a8a;
    --c6: #3a4bd8;
    --c7: #2bb0c4;
    --c8: #c2175b;
  }
  * { box-sizing: border-box; margin: 0; padding: 0; }
  html, body { width: 1200px; height: 900px; overflow: hidden; }
  body {
    background: var(--backdrop);
    font-family: "Open Sans", Arial, sans-serif;
    position: relative;
  }
  .card {
    position: absolute;
    left: 320px;
    width: 560px;
    height: 340px;
    background: var(--card);
    border: 1px solid var(--card-edge);
    box-shadow: 0 12px 30px rgba(0,0,0,.55);
  }
  .card--back { top: 60px; }
  .card--front { top: 480px; }

  /* Back */
  .brand {
    display: flex;
    align-items: center;
    gap: 10px;
    color: var(--red);
    font-weight: 700;
  }
  .brand__dot {
    width: 26px; height: 26px;
    border-radius: 50%;
    background: var(--red);
  }
  .card--back .brand {
    position: absolute;
    top: 26px; right: 92px;
    font-size: 26px;
    letter-spacing: 1px;
  }
  .card--back .top-rule {
    position: absolute;
    top: 42px; right: 20px;
    width: 62px; height: 2px;
    background: var(--red-line);
  }
  .card--back .side-rule {
    position: absolute;
    top: 36px; left: 34px;
    width: 3px; height: 150px;
    background: var(--red-line);
  }
  .service-title {
    position: absolute;
    top: 196px; left: 56px;
    color: var(--red);
    font-size: 26px;
    font-weight: 400;
  }
  .services {
    position: absolute;
    top: 240px; left: 56px;
    font-family: "Tinos", "Times New Roman", serif;
    font-style: italic;
    font-weight: 700;
    font-size: 18px;
    color: var(--text-light);
  }
  .services .initial { color: var(--red); }
  .contacts {
    position: absolute;
    top: 290px; left: 56px;
    display: flex;
    gap: 22px;
    font-size: 13px;
    color: var(--text-muted);
  }
  .contact { display: flex; align-items: center; gap: 7px; }
  .contact svg { width: 16px; height: 16px; }

  /* Front */
  .front-rule {
    position: absolute;
    height: 3px;
    background: var(--red-line);
  }
  .front-rule--left { top: 138px; left: 20px; width: 170px; }
  .front-rule--right { top: 192px; right: 20px; width: 150px; }
  .card--front .brand {
    position: absolute;
    top: 118px; left: 205px;
    font-size: 50px;
    letter-spacing: 2px;
    line-height: 1;
    gap: 14px;
  }
  .card--front .brand__dot { width: 46px; height: 46px; }
  .tagline {
    position: absolute;
    top: 196px; left: 0; right: 0;
    text-align: center;
    font-family: "Tinos", "Times New Roman", serif;
    font-size: 22px;
    letter-spacing: 9px;
    font-weight: 400;
  }
</style>
</head>
<body>
  <section class="card card--back" aria-label="Card back">
    <div class="brand"><span class="brand__dot"></span>DURESK</div>
    <div class="top-rule"></div>
    <div class="side-rule"></div>
    <h2 class="service-title">Personalised Art</h2>
    <p class="services">• <span class="initial">P</span>ortraits • <span class="initial">M</span>urals • <span class="initial">F</span>ashion Illustration</p>
    <div class="contacts">
      <span class="contact">
        <svg viewBox="0 0 16 16" aria-hidden="true"><rect x="4" y="1" width="8" height="14" rx="1.5" fill="none" stroke="currentColor" stroke-width="1.3"/><circle cx="8" cy="12.5" r=".9" fill="currentColor"/></svg>
        0437 582 190
      </span>
      <span class="contact">
        <svg viewBox="0 0 16 16" aria-hidden="true"><rect x="1" y="3.5" width="14" height="9" fill="currentColor"/><path d="M1 3.5 8 9l7-5.5" fill="none" stroke="#1f1f20" stroke-width="1.2"/></svg>
        duresk@duresk.com.au
      </span>
      <span class="contact">
        <svg viewBox="0 0 16 16" aria-hidden="true" fill="none" stroke="currentColor" stroke-width="1.1"><circle cx="8" cy="8" r="6.5"/><ellipse cx="8" cy="8" rx="3" ry="6.5"/><path d="M1.5 8h13"/></svg>
        www.duresk.com.au
      </span>
    </div>
  </section>

  <section class="card card--front" aria-label="Card front">
    <div class="front-rule front-rule--left"></div>
    <div class="brand"><span class="brand__dot"></span>DURESK</div>
    <div class="front-rule front-rule--right"></div>
    <p class="tagline"><span style="color:var(--c1)">L</span><span style="color:var(--c2)">I</span><span style="color:var(--c3)">V</span><span style="color:var(--c4)">I</span><span style="color:var(--c3)">N</span><span style="color:var(--c5)">G</span> <span style="color:var(--c6)">I</span><span style="color:var(--c3)">N</span> <span style="color:var(--c7)">C</span><span style="color:var(--c2)">O</span><span style="color:var(--c5)">L</span><span style="color:var(--c4)">O</span><span style="color:var(--c6)">U</span><span style="color:var(--c8)">R</span></p>
  </section>
</body>
</html>
```